dorwial business card design so that it looks better

need a new business card designed. use our website, dorwian.com for example. I attached an example of a previous card we had and liked. this is for law enforcement and we have attached a previous business card as an example. This site forces me to select color and font, ignore those as I picked stuff just to get this completed.

Target Market(s)

law enforcement, local government

Contact Information for Business Card

see the attached example and our website

Font styles to use
Serif

```html
<!DOCTYPE html>
<html lang="en">
<head>
<meta charset="utf-8">
<title>Dorwial Business Card</title>
<link rel="stylesheet" href="https://fonts.googleapis.com/css2?family=Roboto:wght@300;400;700&display=swap">
<style>
  :root {
    --backdrop: #4a4a4a;
    --card: #151515;
    --card-soft: #1d1d1d;
    --ink: #ffffff;
    --ink-muted: #e2e2e2;
    --silver: #d4d4d4;
  }
  html, body {
    margin: 0;
    padding: 0;
    width: 963px;
    height: 1200px;
    overflow: hidden;
    background: var(--backdrop);
    font-family: "Roboto", Arial, sans-serif;
  }
  .canvas {
    position: relative;
    width: 963px;
    height: 1200px;
  }
  .card {
    position: absolute;
    left: 232px;
    width: 556px;
    height: 317px;
    background: var(--card);
    color: var(--ink);
  }
  .card-front { top: 221px; }
  .card-back { top: 636px; }

  .person {
    position: absolute;
    top: 38px;
    right: 38px;
    text-align: right;
  }
  .person-name {
    margin: 0;
    font-size: 21px;
    font-weight: 700;
    line-height: 1.1;
  }
  .person-title {
    margin: 2px 0 0;
    font-size: 14px;
    font-weight: 400;
    color: var(--ink-muted);
  }
  .contact {
    position: absolute;
    left: 37px;
    bottom: 38px;
    margin: 0;
    font-size: 14px;
    font-weight: 400;
    line-height: 24px;
    font-style: normal;
  }

  .back-texture {
    position: absolute;
    inset: 0;
    background: radial-gradient(ellipse at center, var(--card-soft) 0%, var(--card) 75%);
  }
  .brand-name {
    position: absolute;
    left: 0;
    right: 0;
    top: 50%;
    transform: translateY(-50%);
    margin: 0;
    text-align: center;
    font-size: 44px;
    font-weight: 300;
    letter-spacing: 6px;
    color: var(--silver);
  }
</style>
</head>
<body>
<main class="canvas">
  <section class="card card-front">
    <div class="person">
      <p class="person-name">Daniel Harlow</p>
      <p class="person-title">President</p>
    </div>
    <address class="contact">
      4185 Brookmere Lane, Dallas, TX 75201<br>
      P. 555.214.7730 E. info@dorwian.com W. www.dorwian.com
    </address>
  </section>

  <section class="card card-back">
    <div class="back-texture" role="img" aria-label="Faint tone-on-tone background texture"></div>
    <p class="brand-name">DORWIAL</p>
  </section>
</main>
</body>
</html>
```